Letterhead Design for Vostrana Corporate Stationery

We are seeking a talented designer on ArtHarbor to create a professional and cohesive corporate stationery set for our company, Vostrana. Vostrana is a prominent player in the Commercial Real Estate industry, and we need stationery that reflects our brand's excellence and professionalism.

Scope of Work:

1. Letterhead Template (Microsoft Word):

Design a letterhead template in Microsoft Word format that adheres to our brand standards (attached in project files).
Include all necessary elements such as company logo, address, contact information, and any other relevant details.
The letterhead should be clean, elegant, and suitable for official business correspondence.

2. Business Cards:

Design business cards for our team members using the provided brand guidelines.
Include name, title, contact information, and the Vostrana logo.
Create a design that leaves a lasting impression and reflects our brand's professionalism.

3. Envelopes:

Design envelopes in various sizes (e.g., standard letter and legal sizes) that match the overall stationery theme.
Ensure that the design includes our company name, logo, and return address in accordance with brand guidelines.

4. Stationery:

Create a visually appealing stationery template that can be used for various documents and correspondence.
Ensure that the stationery design aligns with our brand standards and maintains consistency across all materials.

Submission Requirements:

Provide high-resolution files for each item (letterhead, business cards, envelopes, and stationery) in formats suitable for both print and digital use.
Include editable source files (e.g., Adobe Illustrator, Photoshop) for future modifications if necessary.

Design Guidelines:

Our brand is known for professionalism, trustworthiness, and excellence in the Commercial Real Estate industry. Please adhere to the brand standards provided in the project attachments.
Use our company colors, fonts, and logo as specified in the brand guidelines.
Feel free to be creative within the boundaries of our brand to make our stationery stand out while maintaining a professional look.

Budget and Timeline:

We are looking for high-quality designs at a competitive price.
The project timeline is flexible, but we would appreciate prompt responses from designers.
Please submit your best pricing and estimated delivery times with your proposals.
We look forward to receiving your creative and professional designs that will represent Vostrana in the best possible light. Thank you for considering our project, and we can't wait to see your submissions on ArtHarbor!

Target Market(s)

Our primary target market for the corporate stationery design project includes, but is not limited to: Investors: Individuals or entities interested in commercial real estate investment opportunities. Brokers: Commercial real estate brokers who facilitate property transactions and negotiations. Tenant Representatives: Professionals who advocate for the interests of tenants in commercial lease transactions. Lenders: Financial institutions and lenders involved in providing financing for commercial real estate projects. Property Owners: Owners of commercial real estate properties seeking professional correspondence materials. Industry Partners: Professionals and organizations within the commercial real estate industry who collaborate with or provide services to Vostrana. Prospective Clients: Potential clients or partners exploring opportunities in the commercial real estate sector. Please note that while these are the primary target market segments, the stationery design should also appeal to a broader audience within the commercial real estate industry and convey professionalism and trustworthiness to all stakeholders.

Industry/Entity Type

Commercial Real Estate

Font styles to use
Sans Serif

Colors
0054AA
0677BA
7BADD7
CADEEF
E8F1F8
0094D4
00A9DD
6FCCEA
C7EBF8
E9F6FB
F0912C
F2A743
F7CA91
FBE8D2
FDF5EE
EE7325
F08F49
F5BC92
FAE3D3
FDF4ED

Requirements
Must have
• Brand Consistency: Ensure that the design adheres to Vostrana's existing brand standards and guidelines (provided in project attachments). Professional Appearance: The stationery must convey professionalism, trustworthiness, and excellence in the Commercial Real Estate industry. Logo Usage: Integrate the Vostrana logo prominently and appropriately on all stationery items. Contact Information: Include accurate contact details, such as the company's address, phone number, email address, and website URL. Typography: Use the specified fonts from the brand guidelines for all text elements, maintaining consistency in font style and size. Color Palette: Utilize the designated brand colors consistently throughout the design. File Formats: Ensure that the final design files are provided in high-resolution formats suitable for both print and digital use. Also, request editable source files (e.g., Adobe Illustrator, Photoshop) for future modifications if needed. Print-Ready: Prepare the design files to be print-ready, including the appropriate bleed and margin specifications for printing purposes. Stationery Variations: Include designs for letterhead, business cards, envelopes (multiple sizes if applicable), and general stationery. Creativity within Brand Guidelines: Encourage designers to be creative while working within the boundaries of Vostrana's brand standards, making the stationery unique and eye-catching. Versatility: Ensure that the stationery can be easily adapted for various purposes, such as formal business correspondence, presentations, and more. Timely Delivery: Specify your preferred timeline for receiving initial design concepts and revisions. Budget: Indicate your budget range for the project to attract designers who can provide high-quality work within your financial constraints. Responsive Designers: Request that designers are responsive to messages and able to make necessary revisions in a timely manner.
Nice to have
• Creative Elements: Incorporate unique and creative design elements that align with Vostrana's brand identity and the Commercial Real Estate industry. Texture or Embossing: If applicable and within budget, consider incorporating textured or embossed elements to add a tactile dimension to the stationery. Custom Illustrations: Include custom illustrations or graphics that convey the essence of the commercial real estate industry or your company's mission and values. Watermark or Background Pattern: Consider adding a subtle watermark or background pattern that complements the overall design without distracting from the content. Custom Typography: Explore the use of custom typography or stylized lettering for headers or key text elements to make the stationery more visually appealing. Enhanced Print Options: If budget allows, opt for premium printing techniques like foil stamping, spot UV, or letterpress to make the stationery truly stand out. Digital Templates: Request digital templates for electronic documents, such as Microsoft Word templates, PowerPoint templates, or PDF templates, to maintain consistency in digital communications. Multiple Design Concepts: Ask for variations of the stationery design to choose from, providing you with options for different occasions or purposes. QR Codes: If relevant, consider incorporating QR codes that link to Vostrana's website, portfolio, or contact information for convenient access. Environmentally Friendly Options: Explore eco-friendly printing materials and practices to align with sustainability goals, if applicable. Mobile Optimization: Ensure that any digital templates or elements are optimized for mobile use, enhancing accessibility and usability. Social Media Icons: Include social media icons and links to Vostrana's social media profiles, if desired, for a comprehensive online presence. Alternate Color Schemes: Request variations of the design with alternate color schemes for seasonal or special occasions.
Should not have
• Non-Compliance with Brand Guidelines: Specify that the design must strictly adhere to Vostrana's brand guidelines, and any deviations are not acceptable. Excessive Complexity: Avoid overly complex designs that may clutter the stationery or distract from the essential information. Inconsistent Branding: Ensure that all design elements, including colors, fonts, and logo usage, remain consistent with the provided brand standards. Unapproved Fonts: Specify that designers should only use the approved fonts from the brand guidelines and avoid introducing new fonts. Inappropriate Imagery: Request that designers refrain from using images, illustrations, or graphics that are unrelated to the Commercial Real Estate industry or that could potentially be perceived as unprofessional. Overly Bright Colors: If it doesn't align with your brand, discourage the use of overly bright or neon colors that may not convey professionalism. Clashing Color Schemes: Ensure that the color scheme chosen for the design is harmonious and avoids color combinations that clash or are difficult to read. Overuse of Effects: Discourage excessive use of visual effects, such as gradients, drop shadows, or excessive transparency, which can make the stationery appear cluttered. Extravagant Printing Costs: Specify that designers should consider budget constraints and avoid design elements that would significantly increase printing costs, unless the budget allows for premium printing techniques. Outdated Design Trends: Request that the design avoids incorporating outdated design trends that may make the stationery appear dated. Inconsistent Branding Across Items: Ensure that the design maintains consistency across all stationery items (letterhead, business cards, envelopes, etc.) and that there are no significant variations that could create confusion. Overly Busy Layouts: Ask for designs that have a clean and professional appearance, avoiding overcrowded layouts that make it difficult to read or find essential information.

```html
<!DOCTYPE html>
<html lang="en">
<head>
<meta charset="utf-8">
<title>Vostrana Business Card</title>
<link href="https://fonts.googleapis.com/css2?family=Inter:wght@400;700;800&display=swap" rel="stylesheet">
<style>
  :root {
    --page-bg: #e6e8ec;
    --card-bg: #ffffff;
    --navy: #0d2357;
    --brand-blue: #2f78c4;
    --text-grey: #3a3d44;
    --card-shadow: rgba(20, 24, 36, 0.18);
  }
  * { margin: 0; padding: 0; box-sizing: border-box; }
  html, body {
    width: 1200px;
    height: 947px;
    overflow: hidden;
    background: var(--page-bg);
    font-family: "Inter", Arial, sans-serif;
  }
  .stage {
    width: 1200px;
    height: 947px;
    display: flex;
    flex-direction: column;
    align-items: center;
    justify-content: center;
    gap: 64px;
  }
  .card {
    width: 620px;
    height: 354px;
    background: var(--card-bg);
    border-radius: 24px;
    box-shadow: 0 10px 30px var(--card-shadow);
    position: relative;
    display: flex;
    align-items: center;
  }
  .card--front { justify-content: center; }
  .wordmark {
    display: flex;
    align-items: center;
    gap: 14px;
    color: var(--navy);
    font-weight: 800;
    letter-spacing: 0.14em;
    text-transform: uppercase;
  }
  .wordmark__dot {
    border-radius: 50%;
    background: var(--brand-blue);
    flex: none;
  }
  .card--front .wordmark { font-size: 46px; }
  .card--front .wordmark__dot { width: 34px; height: 34px; }

  .card--back { padding: 0 44px 0 40px; }
  .card--back .wordmark { font-size: 28px; width: 270px; justify-content: center; gap: 10px; }
  .card--back .wordmark__dot { width: 22px; height: 22px; }
  .divider {
    width: 2px;
    height: 210px;
    background: var(--brand-blue);
    margin: 0 30px 0 14px;
    flex: none;
  }
  .contact { color: var(--text-grey); }
  .contact__name {
    color: var(--brand-blue);
    font-weight: 800;
    font-size: 25px;
    letter-spacing: 0.01em;
    text-transform: uppercase;
    line-height: 1.1;
  }
  .contact__title { font-size: 15px; margin-top: 4px; }
  .contact__list { list-style: none; margin-top: 18px; font-size: 15px; line-height: 1.6; }
  .contact__list li { display: flex; align-items: center; gap: 9px; }
  .contact__icon { width: 13px; height: 13px; fill: var(--brand-blue); flex: none; }
  .contact__address { margin-top: 18px; font-size: 15px; line-height: 1.5; }
</style>
</head>
<body>
<main class="stage">
  <section class="card card--front" aria-label="Business card front">
    <div class="wordmark"><span class="wordmark__dot"></span>Vostrana</div>
  </section>

  <section class="card card--back" aria-label="Business card back">
    <div class="wordmark"><span class="wordmark__dot"></span>Vostrana</div>
    <div class="divider"></div>
    <div class="contact">
      <p class="contact__name">Marcus Hale</p>
      <p class="contact__title">Managing Director</p>
      <ul class="contact__list">
        <li>
          <svg class="contact__icon" viewBox="0 0 24 24" aria-hidden="true"><path d="M6.6 10.8a15.1 15.1 0 0 0 6.6 6.6l2.2-2.2a1 1 0 0 1 1-.25 11.4 11.4 0 0 0 3.6.57 1 1 0 0 1 1 1V20a1 1 0 0 1-1 1A17 17 0 0 1 3 4a1 1 0 0 1 1-1h3.5a1 1 0 0 1 1 1c0 1.25.2 2.45.57 3.57a1 1 0 0 1-.25 1z"/></svg>
          123 555 0147
        </li>
        <li>
          <svg class="contact__icon" viewBox="0 0 24 24" aria-hidden="true"><path d="M2 5h20v14H2z M2 5l10 8 10-8" /><path d="M2 6l10 7.5L22 6v1.5l-10 7.5L2 7.5z" fill="#fff"/></svg>
          info@vostranamail.com
        </li>
        <li>
          <svg class="contact__icon" viewBox="0 0 24 24" aria-hidden="true"><circle cx="12" cy="12" r="10"/><path d="M2 12h20M12 2c3 3 3 17 0 20M12 2c-3 3-3 17 0 20" stroke="#fff" stroke-width="1.6" fill="none"/></svg>
          www.vostrana-site.com
        </li>
      </ul>
      <p class="contact__address">Your address, City<br>State, Zip 1234</p>
    </div>
  </section>
</main>
</body>
</html>
```